Business card Zottelgarten

Business card is for a self-employed dog trainer with own dog school. Name and logo of the dog school are available. Color specifications as well. The design should be classy and minimalist, but also modern. An already existing idea would be: Front: Only the logo Back: Contact data

Font styles to use
Serif
Sans Serif
Other font styles liked:
• Trajan Pro

Colors
f78f20

Requirements
Must have
• Name: Margit Wendler-Rasch Title: Dipl. Dog Trainer Contain my logo Follow my font and color preferences (see files)

```html
<!DOCTYPE html>
<html lang="de">
<head>
<meta charset="utf-8">
<title>Zottelgarten – Visitenkarte</title>
<link rel="stylesheet" href="https://fonts.googleapis.com/css2?family=Cinzel:wght@400;600&family=Open+Sans:wght@400;600&display=swap">
<style>
  :root {
    --orange: #f78f20;
    --ink: #221f20;
    --white: #ffffff;
    --stage: #2b2d2c;
    --text-light: #f4f4f4;
  }
  * { margin: 0; padding: 0; box-sizing: border-box; }
  html, body {
    width: 1200px; height: 1200px; overflow: hidden;
    background: var(--stage);
  }
  .canvas { position: relative; width: 1200px; height: 1200px; }
  .card {
    position: absolute; left: 250px; width: 700px; height: 400px;
    overflow: hidden;
    box-shadow: 0 14px 30px rgba(0,0,0,.35);
  }

  /* Front */
  .card-front { top: 130px; background: var(--orange); }
  .brand {
    position: absolute; left: 50%; top: 50%;
    transform: translate(-50%, -50%);
    display: flex; align-items: center; gap: 22px;
  }
  .brand-words { display: flex; flex-direction: column; align-items: flex-start; }
  .brand-name {
    font-family: "Cinzel", serif; font-weight: 400;
    font-size: 48px; letter-spacing: 2px; color: var(--white); line-height: 1;
    white-space: nowrap;
  }
  .brand-url {
    font-family: "Cinzel", serif; font-weight: 400;
    font-size: 11px; letter-spacing: 12.6px; color: var(--white);
    margin-top: 10px; white-space: nowrap;
  }
  .brand-circle {
    width: 150px; height: 150px; border-radius: 50%; flex: none;
    background: var(--white);
    box-shadow: 0 0 0 5px var(--orange), 0 0 0 7px var(--white);
  }

  /* Back */
  .card-back { top: 640px; background: var(--ink); }
  .accent-bar {
    position: absolute; left: 0; top: 58px; width: 64px; height: 14px;
    background: var(--orange);
  }
  .contact {
    position: absolute; left: 88px; top: 48px;
    font-family: "Open Sans", sans-serif; color: var(--text-light);
  }
  .person { font-size: 22px; font-weight: 600; line-height: 1.4; }
  .role { font-size: 17px; line-height: 1.4; margin-bottom: 22px; }
  .line {
    display: flex; align-items: center; gap: 10px;
    font-size: 18px; line-height: 1.5; margin-bottom: 4px; margin-left: -30px;
  }
  .icon { width: 20px; height: 20px; flex: none; }
  .bottom-band { position: absolute; left: 0; bottom: 0; width: 700px; height: 44px; }
</style>
</head>
<body>
<main class="canvas">

  <section class="card card-front" aria-label="Vorderseite">
    <div class="brand">
      <div class="brand-words">
        <span class="brand-name">ZOTTELGARTEN</span>
        <span class="brand-url">WWW.ZOTTELGARTEN.CH</span>
      </div>
      <div class="brand-circle"></div>
    </div>
  </section>

  <section class="card card-back" aria-label="Rückseite">
    <div class="accent-bar"></div>
    <div class="contact">
      <p class="person">Margit Wendler-Rasch</p>
      <p class="role">Dipl. Dog Trainer</p>
      <p class="line">
        <svg class="icon" viewBox="0 0 20 20" aria-hidden="true">
          <circle cx="10" cy="10" r="10" fill="var(--orange)"/>
          <rect x="7" y="4.5" width="6" height="11" rx="1.2" fill="none" stroke="#fff" stroke-width="1.5"/>
          <circle cx="10" cy="13.3" r=".8" fill="#fff"/>
        </svg>
        123 456 7890
      </p>
      <p class="line">
        <svg class="icon" viewBox="0 0 20 20" aria-hidden="true">
          <circle cx="10" cy="10" r="10" fill="var(--orange)"/>
          <circle cx="10" cy="10" r="5" fill="none" stroke="#fff" stroke-width="1.4"/>
          <path d="M5 10h10M10 5c-2.5 3-2.5 7 0 10M10 5c2.5 3 2.5 7 0 10" fill="none" stroke="#fff" stroke-width="1.1"/>
        </svg>
        www.zottelgarten.ch
      </p>
    </div>
    <svg class="bottom-band" viewBox="0 0 700 44" aria-hidden="true">
      <polygon points="150,0 700,0 700,44 150,44 172,22" fill="var(--orange)"/>
    </svg>
  </section>

</main>
</body>
</html>
```